Medical Billing Company Needs a Business Card Design

We need a business card design for a Florida based medical billing company called 'Medora Crestline Solutions'. We specialize in providing revenue cycle management services to physician and therapist offices (we're basically their back-office processing partner for providing billing software, claims submissions, A/R follow-up and patient statements & collections. Our logo is red and blue-ish, so make sure that whatever other elements are used will match appropriately. Our current business card design has a too small font size. I'd like to project an image that shows we are modern & reliable. On a side note, I'm planning on using ZIB for printing these cards.

Target Market(s)

Office managers, physicians, therapists

Industry/Entity Type

Printing

Requirements
Must have
• Logo
Name of Employee
Phone
Fax
E-mail
Website

```html
<!DOCTYPE html>
<html lang="en">
<head>
<meta charset="utf-8">
<title>Medora Crestline Solutions – Stationery</title>
<link href="https://fonts.googleapis.com/css2?family=Open+Sans:wght@400;600&display=swap" rel="stylesheet">
<style>
  :root {
    --navy: #1e0f63;
    --red: #c4000f;
    --white: #ffffff;
    --rule: #d6d6d6;
    --shadow: #555555;
    --text-soft: #4a4a5a;
    --sky-top: #ffffff;
    --sky-bottom: #b9b9b9;
    --floor-top: #e2e2e2;
    --floor-bottom: #aeaeae;
    --divider: #f2f2f2;
  }
  * { margin: 0; padding: 0; box-sizing: border-box; }
  html, body { width: 1200px; height: 900px; overflow: hidden; }
  body {
    position: relative;
    font-family: "Open Sans", Arial, sans-serif;
    background: var(--floor-bottom);
  }
  .header-band {
    position: absolute; left: 0; top: 0; width: 1200px; height: 264px;
    background: linear-gradient(to bottom, var(--sky-top) 0%, #e6e6e6 35%, var(--sky-bottom) 100%);
    display: flex; align-items: center; justify-content: center;
  }
  .band-divider {
    position: absolute; left: 0; top: 264px; width: 1200px; height: 8px;
    background: linear-gradient(to bottom, var(--divider), #c9c9c9);
  }
  .lower-band {
    position: absolute; left: 0; top: 272px; width: 1200px; height: 628px;
    background: linear-gradient(to bottom, var(--floor-top), var(--floor-bottom));
  }

  .brand { display: flex; align-items: center; white-space: nowrap; }
  .brand-square { flex: none; background: var(--red); }
  .wordmark {
    color: var(--navy);
    font-weight: 400;
    text-transform: uppercase;
    line-height: 1;
  }
  .header-band .brand { margin-top: -6px; gap: 18px; }
  .header-band .brand-square { width: 30px; height: 30px; }
  .header-band .wordmark { font-size: 42px; letter-spacing: 3.5px; }

  .sheet { position: absolute; background: var(--white); }

  .letterhead { left: 506px; top: 232px; width: 689px; height: 663px; }
  .letterhead .brand { position: absolute; left: 70px; top: 47px; gap: 8px; }
  .letterhead .brand-square { width: 12px; height: 12px; }
  .letterhead .wordmark { font-size: 17px; letter-spacing: 1.4px; }
  .letterhead .head-rule {
    position: absolute; left: 412px; top: 62px; width: 248px; height: 2px; background: var(--navy);
  }
  .letterhead .edge-rule {
    position: absolute; left: 61px; top: 51px; width: 2px; height: 570px; background: var(--shadow);
  }
  .letterhead .footer-band {
    position: absolute; left: 0; bottom: 0; width: 689px; height: 42px; background: var(--red);
    color: var(--white); font-family: Arial, sans-serif; font-size: 13px;
    display: flex; align-items: center; justify-content: center;
  }

  .card {
    position: absolute; left: 101px; width: 465px; height: 266px;
    box-shadow: 3px 3px 0 var(--shadow);
  }
  .card-front { top: 280px; }
  .card-back { top: 580px; display: flex; align-items: center; justify-content: center; }
  .card .brand { gap: 7px; }
  .card .brand-square { width: 11px; height: 11px; }
  .card .wordmark { font-size: 16px; letter-spacing: 1.2px; }
  .card-front .brand { position: absolute; left: 38px; top: 23px; }
  .card-front .head-rule {
    position: absolute; left: 196px; top: 51px; width: 230px; height: 1px; background: var(--rule);
  }
  .card-front .contact {
    position: absolute; left: 38px; top: 78px; width: 390px;
    font-size: 12px; line-height: 1.55; color: var(--text-soft);
  }
  .contact .employee-name { font-size: 16px; font-weight: 600; color: var(--navy); line-height: 1.3; }
  .contact .employee-title { font-size: 12px; color: var(--red); margin-bottom: 8px; }
  .contact .label { display: inline-block; width: 48px; color: var(--navy); font-weight: 600; }
  .card-front .accent-stripe {
    position: absolute; left: 0; top: 223px; width: 465px; height: 7px; background: var(--red);
  }
  .card-front .footer-band {
    position: absolute; left: 0; top: 230px; width: 465px; height: 36px; background: var(--navy);
    color: var(--white); font-family: Arial, sans-serif; font-size: 13px;
    display: flex; align-items: center; justify-content: center;
  }
</style>
</head>
<body>
  <header class="header-band">
    <div class="brand"><span class="brand-square"></span><span class="wordmark">Medora Crestline Solutions</span></div>
  </header>
  <div class="band-divider"></div>
  <div class="lower-band"></div>

  <section class="sheet letterhead" aria-label="Letterhead">
    <div class="edge-rule"></div>
    <div class="brand"><span class="brand-square"></span><span class="wordmark">Medora Crestline Solutions</span></div>
    <div class="head-rule"></div>
    <footer class="footer-band">www.medoracrestline.com</footer>
  </section>

  <section class="sheet card card-front" aria-label="Business card front">
    <div class="brand"><span class="brand-square"></span><span class="wordmark">Medora Crestline Solutions</span></div>
    <div class="head-rule"></div>
    <div class="contact">
      <div class="employee-name">Jordan Ellery</div>
      <div class="employee-title">Account Manager</div>
      <div><span class="label">Phone</span>(555) 014-2270</div>
      <div><span class="label">Fax</span>(555) 014-2271</div>
      <div><span class="label">E-mail</span>jellery@medoracrestline.com</div>
    </div>
    <div class="accent-stripe"></div>
    <footer class="footer-band">www.medoracrestline.com</footer>
  </section>

  <section class="sheet card card-back" aria-label="Business card back">
    <div class="brand"><span class="brand-square"></span><span class="wordmark">Medora Crestline Solutions</span></div>
  </section>
</body>
</html>
```